Wordpress Theme Design for Glacio-Blaze

Hi, I am looking for an awesome WORDPRESS theme for my snoball and coffee business that is called Glacio-Blaze. This has to be a wordpress theme, because I have other plugins that I would like to use with this site. I want the design to be professional and sophisticated, but also appeal to kids, because after all, the main focus of the business is going to be snoballs, which kids love. I don't want it to look too much like a kiddy site, though. I am also going to be selling other items such as frito pies, hotdogs, cotton candy, nachos, pickles, candy, toys, etc, but the main focus will be the hot and cold aspect of the coffee and snoballs (hence the name, "Glacio-Blaze"). I want the design to look very creative/original and really be attractive to kids, but also very professional so that even adults like coming to the site.
Somewhere in the design I would like to be able to advertise other local businesses in the future, so I would like space incorporated into the design for that. I would also like to be able to add other pages if I want, so there should be space along the top for links, such as "home", "contact", etc. It would also be nice to have a footer in the design for links or other plugins. If you take a look at the site http://quirkypuppyclipsz.example/, I like the functionality of the site (for example, the layout, links, footer, sidebar on other pages), but obviously there isn't much custom design with the theme.
I actually already have a logo designed that I would like incorporated into the look and feel of the design, so that should give you a good place to start with your design. I want the graphics in the theme to really be eye-catching. You are more than welcome to tweak my current logo, blend it into the theme, whatever...(if you want half of the page to be frozen, and the other half to be fire-ish, doesn't have to be, just giving ideas...any and all designs I will take into consideration). Basically, whatever you think would look amazing.
The more amazing the design, I would definitely give a bonus for.
If this helps you out, I'm not looking for a "glossy" style of wordpress design. I really like how this site (CraftHerdly) is made. It uses softer, cleaner colors and designs...it's kind of like a "grunge" style with its text and designs (what I mean is it's not a cookie cutter type of design), but nothing too extreme grunge by any means. I'm looking for the same style as the CraftHerdly site, only with the flare of my type of business.
Hope this helps
Thank you
Reason: The designs, although nice, are not really what I am looking for. These all just feel like they are ready made templates, and I'm looking for something a little more original and unique.

```html
<!DOCTYPE html>
<html lang="en">
<head>
<meta charset="utf-8">
<title>Glacio-Blaze</title>
<link rel="stylesheet" href="https://fonts.googleapis.com/css2?family=Open+Sans:ital,wght@0,400;0,600;0,700;1,400&display=swap">
<style>
:root{
  --orange-top:#f4672b;
  --orange-bottom:#e8561c;
  --page-dark:#23282b;
  --footer-dark:#151617;
  --frame-cream:#efe9dc;
  --panel-light:#e2ddd3;
  --panel-side:#aca596;
  --tab-light:#ddd6c9;
  --ink:#333;
  --ink-soft:#444;
  --footer-text:#b9b9b9;
  --footer-muted:#6b6b6b;
  --rule-dark:#2a2b2c;
}
*{box-sizing:border-box;margin:0;padding:0}
html,body{width:873px;height:1200px;overflow:hidden;background:var(--page-dark)}
body{font-family:"Open Sans",Arial,sans-serif}
.page{position:relative;width:918px;height:1262px;transform:scale(0.95098);transform-origin:0 0;background:var(--page-dark)}
.abs{position:absolute}

/* header */
.site-header{left:0;top:0;width:918px;height:87px;background:linear-gradient(var(--orange-top),var(--orange-bottom));box-shadow:0 2px 6px rgba(0,0,0,.5)}
.brand{left:155px;top:34px;display:flex;align-items:center;gap:7px;color:#fff;font-weight:700;font-size:17px}
.brand-dot{width:14px;height:14px;border-radius:50%;background:#fff}
.search{left:611px;top:31px;width:161px;height:17px;background:#eeeeee;color:#888;font-style:italic;font-size:12px;text-align:right;padding-right:7px;line-height:17px}
.main-nav{right:146px;top:60px;display:flex;font-size:12.5px;font-weight:700;color:#fff;white-space:nowrap}
.main-nav span{padding:0 8px;border-left:1px solid rgba(255,255,255,.45);line-height:19px}
.main-nav span:first-child{border-left:0}
.main-nav span:last-child{padding-right:0}

/* gallery */
.photo-frame{top:140px;width:136px;height:166px;background:var(--frame-cream);padding:6px;box-shadow:2px 3px 6px rgba(0,0,0,.5)}
.photo{width:100%;height:100%}

/* content */
.content{left:153px;top:349px;width:619px;height:416px;background:var(--panel-light)}
.sidebar{left:584px;top:349px;width:188px;height:416px;background:var(--panel-side)}
.section-title{font-size:15px;font-weight:700;color:var(--ink);white-space:nowrap}
.copy{font-size:11px;line-height:13.2px;color:var(--ink-soft);width:380px}
.thumb{width:95px;height:84px;background:var(--frame-cream);padding:6px;box-shadow:2px 3px 5px rgba(0,0,0,.35)}
.news-tab{left:604px;width:176px;height:23px;background:var(--tab-light);font-size:12.5px;font-weight:700;color:var(--ink);padding-left:8px;line-height:23px;white-space:nowrap}
.news-tab::after{content:"";position:absolute;right:0;bottom:-6px;border-top:6px solid #7d776c;border-right:8px solid transparent}
.news-copy{left:614px;width:158px;font-size:10.8px;line-height:13.1px;color:#3a3a3a}
.more{left:615px;width:32px;height:11px;background:#e5e0d6;font-size:10px;line-height:11px;color:#444;padding-left:2px}

/* footer */
.site-footer{left:0;top:818px;width:918px;height:444px;background:var(--footer-dark)}
.link-column{top:838px;width:155px}
.link-column h3{font-size:14.5px;font-weight:700;color:#f2f2f2;height:26px;border-bottom:1px solid var(--rule-dark);white-space:nowrap}
.link-column ul{list-style:none;margin-top:8px}
.link-column li{font-size:12.5px;line-height:23px;color:var(--footer-text);white-space:nowrap}
.legal{left:153px;top:1173px;width:619px;height:53px;border-top:1px solid var(--rule-dark);border-bottom:1px solid var(--rule-dark);text-align:center;color:var(--footer-muted);font-size:10.5px;line-height:22px;padding-top:3px;white-space:nowrap;letter-spacing:-0.1px}
</style>
</head>
<body>
<div class="page">
  <header class="site-header abs"></header>
  <div class="brand abs"><span class="brand-dot"></span>Glacio-Blaze</div>
  <div class="search abs">search</div>
  <nav class="main-nav abs"><span>Home</span><span>About Us</span><span>Services</span><span>Contact Us</span></nav>

  <div class="photo-frame abs" style="left:153px"><div class="photo" role="img" aria-label="Cup of coffee on a saucer with coffee beans" style="background:linear-gradient(#d9d2c8,#6b4a30)"></div></div>
  <div class="photo-frame abs" style="left:314px"><div class="photo" role="img" aria-label="Rainbow swirl lollipop and candies" style="background:linear-gradient(135deg,#e54b3a,#f2c23a 40%,#4aa6d8 70%,#6bb84a)"></div></div>
  <div class="photo-frame abs" style="left:475px"><div class="photo" role="img" aria-label="Red and white candy canes" style="background:linear-gradient(#d8303a,#f1c9c9 50%,#c9283a)"></div></div>
  <div class="photo-frame abs" style="left:636px"><div class="photo" role="img" aria-label="Plate of nachos with toppings" style="background:linear-gradient(#4a5a2c,#c88a3a 60%,#2a2420)"></div></div>

  <section class="content abs"></section>
  <aside class="sidebar abs"></aside>

  <h2 class="section-title abs" style="left:165px;top:360px">Welcome to Glacio-Blaze</h2>
  <p class="copy abs" style="left:174px;top:389px">Lorem ipsum dolor sit amet, consectetuer adipiscing elit, sed diam nonummy nibh euismod tincidunt ut laoreet dolore magna aliquam volutpat. Ut wisi enim ad minim veniam, quis nostrud exerci tation ullamcorper suscipit lobortis nisl ut aliquip ex ea commodo consequat.</p>
  <h2 class="section-title abs" style="left:165px;top:471px">Products</h2>
  <p class="copy abs" style="left:174px;top:499px">Lorem ipsum dolor sit amet, consectetuer adipiscing elit, sed diam nonummy nibh euismod tincidunt ut laoreet dolore magna aliquam volutpat. Ut wisi enim ad minim veniam, quis nostrud exerci tation ullamcorper suscipit lobortis nisl ut aliquip ex ea commodo consequat.</p>

  <div class="thumb abs" style="left:169px;top:571px"><div class="photo" role="img" aria-label="Coffee cup" style="background:linear-gradient(#ece7e0,#8a6a4a)"></div></div>
  <div class="thumb abs" style="left:270px;top:571px"><div class="photo" role="img" aria-label="Tipped cup with coffee beans" style="background:linear-gradient(135deg,#8a5a36,#3a2014)"></div></div>
  <div class="thumb abs" style="left:371px;top:571px"><div class="photo" role="img" aria-label="Scoop of ice cream with fruit" style="background:linear-gradient(#f4efe8,#e0a070 60%,#f2ece4)"></div></div>
  <div class="thumb abs" style="left:472px;top:571px"><div class="photo" role="img" aria-label="Chocolate cake slice with cream" style="background:linear-gradient(#f0ebe4,#6a3a22 70%)"></div></div>
  <div class="thumb abs" style="left:169px;top:662px"><div class="photo" role="img" aria-label="Strawberry cheesecake" style="background:linear-gradient(#d83a32,#f4eeea 60%)"></div></div>
  <div class="thumb abs" style="left:270px;top:662px"><div class="photo" role="img" aria-label="Pink frosted cupcakes" style="background:linear-gradient(#e88aa8,#c84a6a 60%,#f0d8e0)"></div></div>
  <div class="thumb abs" style="left:371px;top:662px"><div class="photo" role="img" aria-label="Pile of tortilla chips" style="background:linear-gradient(135deg,#f0c860,#d89a38)"></div></div>
  <div class="thumb abs" style="left:472px;top:662px"><div class="photo" role="img" aria-label="Plate of loaded nachos" style="background:linear-gradient(#1e1a1a,#c84a2a 50%,#e8e0d8)"></div></div>

  <div class="news-tab abs" style="top:361px">Latest News One</div>
  <p class="news-copy abs" style="top:391px">Lorem ipsum dolor sit amet, consectetuer adipiscing elit, sed diam nonummy nibh euismod tincidunt ut laoreet dolore magna aliquam...</p>
  <div class="more abs" style="top:462px">more</div>

  <div class="news-tab abs" style="top:492px">Latest News One</div>
  <p class="news-copy abs" style="top:522px">Lorem ipsum dolor sit amet, consectetuer adipiscing elit, sed diam nonummy nibh euismod tincidunt ut laoreet dolore magna aliquam...</p>
  <div class="more abs" style="top:593px">more</div>

  <div class="news-tab abs" style="top:623px">Latest News One</div>
  <p class="news-copy abs" style="top:653px">Lorem ipsum dolor sit amet, consectetuer adipiscing elit, sed diam nonummy nibh euismod tincidunt ut laoreet dolore magna aliquam...</p>
  <div class="more abs" style="top:724px">more</div>

  <footer class="site-footer abs"></footer>
  <div class="link-column abs" style="left:153px"><h3>Popular Search</h3><ul><li>Glacio-Blaze</li><li>Coffee</li><li>Cold Coffee</li><li>Glacio-Blaze</li><li>Coffee</li><li>Cold Coffee</li><li>Glacio-Blaze</li><li>Coffee</li><li>Cold Coffee</li><li>Glacio-Blaze</li><li>Coffee</li><li>Cold Coffee</li></ul></div>
  <div class="link-column abs" style="left:324px"><h3>Popular Search</h3><ul><li>Glacio-Blaze</li><li>Coffee</li><li>Cold Coffee</li><li>Glacio-Blaze</li><li>Coffee</li><li>Cold Coffee</li><li>Glacio-Blaze</li><li>Coffee</li><li>Cold Coffee</li><li>Glacio-Blaze</li><li>Coffee</li><li>Cold Coffee</li></ul></div>
  <div class="link-column abs" style="left:495px"><h3>Popular Search</h3><ul><li>Glacio-Blaze</li><li>Coffee</li><li>Cold Coffee</li><li>Glacio-Blaze</li><li>Coffee</li><li>Cold Coffee</li><li>Glacio-Blaze</li><li>Coffee</li><li>Cold Coffee</li><li>Glacio-Blaze</li><li>Coffee</li><li>Cold Coffee</li></ul></div>
  <div class="link-column abs" style="left:666px;width:106px"><h3>Popular Search</h3><ul><li>Glacio-Blaze</li><li>Coffee</li><li>Cold Coffee</li><li>Glacio-Blaze</li><li>Coffee</li><li>Cold Coffee</li><li>Glacio-Blaze</li><li>Coffee</li><li>Cold Coffee</li><li>Glacio-Blaze</li><li>Coffee</li><li>Cold Coffee</li></ul></div>

  <div class="legal abs">Copyright 2012 &nbsp;|&nbsp; All Rights Reserved<br>Anti-spam policy | Disclaimer | Dmca notice | Email Policy | Earnings Disclaimer | External Links Policy | Testimonials</div>
</div>
</body>
</html>
```